Summer Sunglass offer

Need a poster design for a spring / summer campaign. We are an opticians with good footfall. The design needs to be eye catching and aimed at 40 year old plus. The offer is Up to 50% off sunglass offer, t&c apply. (I have attached our last year campaign)
Also need a 2 sided A5 leaflet design (see attached)
I've uploaded a copy of our logo

A5 leaflet should read:

Grab a bargain on two great looks this summer Upto 50% off sunglasses
Look great and stay safe in the sun this summer

We want you to look great, feel fantastic and most of all stay safe in the sun this summer. That’s why we’re offering you 50% off prescription sunglasses with every complete pair of glasses you buy this summer or 25% off for prescription sunglasses with no other purchase.
Find you new summer looks from our gorgeous collection of frames in store. It matters to us that you look great in your new glasses as much as how well you see through them, so we’ll be on hand to help you find frames that suit you best.
What new looks will you go for? Smart or sassy? Formal or Fun? Whatever you’re in the mood for, you’ll find it in our collections this summer.
Call in today to find your new looks, and remember to bring your prescription if you don’t need an eye test.

Target Market(s)

40 + year old

Industry/Entity Type

Optician

Colors

Designer to choose colors to be used in the design.

Requirements
Must have
• Images, preferably a male and Female image

```html
<!DOCTYPE html>
<html lang="en">
<head>
<meta charset="utf-8">
<title>Summer Sunglass Offer Poster</title>
<link href="https://fonts.googleapis.com/css2?family=Poppins:wght@300;400;500;600&display=swap" rel="stylesheet">
<style>
  :root {
    --teal-top: #86e6e9;
    --teal-bottom: #78d3d5;
    --white: #ffffff;
    --brand-blue: #2b3f95;
    --brand-teal: #4fa9b1;
    --photo-light: #b9c9c8;
    --photo-warm: #d9c9a3;
  }
  * { margin: 0; padding: 0; box-sizing: border-box; }
  html, body { width: 890px; height: 1200px; overflow: hidden; background: var(--white); }
  body { font-family: "Poppins", sans-serif; }
  .poster { position: relative; width: 890px; height: 1200px; }
  .hero {
    position: absolute; left: 0; top: 0; width: 890px; height: 964px;
    background: linear-gradient(180deg, var(--teal-top), var(--teal-bottom));
    overflow: hidden;
  }
  .hero-frame { position: absolute; left: 0; top: 0; }
  .kicker {
    position: absolute; left: 77px; top: 57px;
    color: var(--white); font-weight: 400; font-size: 42px; letter-spacing: 26px;
    white-space: nowrap; line-height: 1;
  }
  .upto {
    position: absolute; left: 76px; top: 117px;
    color: var(--white); font-weight: 600; font-size: 86px; line-height: 1; letter-spacing: -2px;
  }
  .big-number {
    position: absolute; left: 50px; top: 146px;
    color: var(--white); font-weight: 500; font-size: 438px; line-height: 1; letter-spacing: -24px;
  }
  .percent {
    position: absolute; left: 562px; top: 178px;
    color: var(--white); font-weight: 600; font-size: 210px; line-height: 1;
  }
  .off {
    position: absolute; left: 574px; top: 390px;
    color: var(--white); font-weight: 600; font-size: 140px; line-height: 1; letter-spacing: -3px;
  }
  .terms-tag {
    position: absolute; left: 820px; top: 900px;
    transform: rotate(-90deg); transform-origin: left top;
    color: var(--white); font-size: 12px; font-weight: 400; white-space: nowrap;
  }
  .photo {
    position: absolute; left: 110px; top: 528px; width: 670px; height: 436px;
    border-radius: 140px 140px 0 0;
    background: linear-gradient(180deg, var(--photo-light) 0%, #e9ecea 45%, var(--photo-warm) 100%);
  }
  .footer {
    position: absolute; left: 0; top: 964px; width: 890px; height: 236px;
    display: flex; flex-direction: column; align-items: center;
  }
  .brand { display: flex; align-items: center; gap: 14px; margin-top: 78px; }
  .brand-dot { width: 34px; height: 34px; border-radius: 50%; background: var(--brand-teal); }
  .brand-name {
    color: var(--brand-blue); font-weight: 500; font-size: 30px; letter-spacing: 2px; line-height: 1;
  }
  .website {
    margin-top: 34px; color: var(--brand-blue); font-weight: 600; font-size: 17px; letter-spacing: 6px;
  }
  .fine-print {
    margin-top: 16px; color: var(--brand-teal); font-weight: 300; font-size: 11.2px;
    line-height: 15px; text-align: center;
  }
</style>
</head>
<body>
<main class="poster">
  <section class="hero">
    <svg class="hero-frame" width="890" height="964" viewBox="0 0 890 964" aria-hidden="true">
      <polyline points="365,133 806,133 806,350" fill="none" stroke="#ffffff" stroke-width="6"/>
      <polyline points="806,557 806,898 80,898 80,535" fill="none" stroke="#ffffff" stroke-width="6"/>
    </svg>
    <div class="kicker">SUMMER SUNGLASS</div>
    <div class="upto">UPTO</div>
    <div class="big-number">50</div>
    <div class="percent">%</div>
    <div class="off">OFF</div>
    <div class="photo" role="img" aria-label="Smiling man and woman in sunglasses and sun hats, he holds a camera and she holds a beach ball"></div>
    <div class="terms-tag">T&amp;C APPLY</div>
  </section>
  <footer class="footer">
    <div class="brand">
      <span class="brand-dot"></span>
      <span class="brand-name">HARWELL EYECARE CENTRE</span>
    </div>
    <div class="website">www.harwelleyecare.co.uk</div>
    <p class="fine-print">*Offer includes frame from selected range, standard single vision lenses, tint and uv protection.<br>Lens upgrades available at extra cost Offer excludes Coral Bay frames. Cannot be used with any other offer.</p>
  </footer>
</main>
</body>
</html>
```